Transport & Storage Company needs a revamp of current card

Would like to keep same colours & basic design but would like to "sharpen" up look of card.

Please remove "The Bright Haulers"

Please add 1800 419 386 on front & back of card

Please add email address on back of card - martin@brackenfreight.com.au

I would like our ABN No - 83 214 976 302 on back of card (which currently has logo only). Logo on back of card can be removed if insufficient space.

Please design another card (same as above) but with Donna Petherick - 0438 562 714, donna@brackenfreight.com.au

I do not want cards to look "too busy" so please re-arrange layout of card if necessary.

Target Market(s)

Transport & Storage

Industry/Entity Type

It Company

Contact Information for Business Card

Please refer to attached current business card

Font styles to use
Other font styles liked:
• Tahoma

Requirements
Must have
• Refer to project decsription
Nice to have
Should not have

```html
<!DOCTYPE html>
<html lang="en">
<head>
<meta charset="utf-8">
<title>Bracken Freight – Business Cards</title>
<link href="https://fonts.googleapis.com/css2?family=Noto+Sans:wght@400;700&display=swap" rel="stylesheet">
<style>
  :root {
    --bg: #d3d3d6;
    --card-white: #ffffff;
    --brand-purple: #7b5aa6;
    --lavender: rgba(183, 162, 214, 0.55);
    --lavender-soft: rgba(232, 224, 242, 0.35);
    --bullet: #d4cce3;
    --text-light: #ffffff;
    --shadow: rgba(0, 0, 0, 0.22);
  }
  * { margin: 0; padding: 0; box-sizing: border-box; }
  html, body { width: 1200px; height: 720px; overflow: hidden; }
  body {
    background: var(--bg);
    position: relative;
    font-family: "Noto Sans", Tahoma, sans-serif;
  }
  .card {
    position: absolute;
    width: 504px;
    height: 286px;
    background: var(--brand-purple);
    box-shadow: 0 3px 8px var(--shadow);
    overflow: hidden;
  }
  .card--front.card--left { left: 67px; top: 60px; }
  .card--front.card--right { left: 628px; top: 60px; }
  .card--back.card--left { left: 67px; top: 375px; }
  .card--back.card--right { left: 628px; top: 375px; }

  .card__header {
    position: absolute; left: 0; top: 0; width: 100%;
    background: var(--card-white);
  }
  .card--front .card__header { height: 95px; }
  .card--back .card__header { height: 143px; }

  .card__accent {
    position: absolute; top: 0; height: 286px; width: 170px;
    background: linear-gradient(200deg, var(--lavender) 0%, var(--lavender-soft) 45%, rgba(255,255,255,0) 85%);
  }
  .card--front .card__accent { left: 300px; }
  .card--back .card__accent { left: 320px; }

  .brand {
    position: absolute;
    color: var(--brand-purple);
    font-weight: 700;
    white-space: nowrap;
    line-height: 1;
  }
  .card--front .brand { left: 34px; top: 33px; font-size: 26px; }
  .card--back .brand { left: 50px; top: 52px; font-size: 34px; }

  .holder {
    position: absolute; left: 40px; top: 151px;
    color: var(--text-light); font-size: 17px; font-weight: 700;
  }
  .contact-list {
    position: absolute; left: 38px; list-style: none;
    color: var(--text-light); font-size: 14px; line-height: 20px;
  }
  .card--front .contact-list { top: 183px; }
  .card--back .contact-list { top: 183px; }
  .contact-list li, .website { display: flex; align-items: center; }
  .contact-list li::before, .website::before {
    content: ""; width: 9px; height: 9px; border-radius: 50%;
    background: var(--bullet); margin-right: 7px; flex: none;
  }
  .website {
    position: absolute; left: 246px; top: 240px;
    color: var(--text-light); font-size: 14px;
  }
</style>
</head>
<body>

<section class="card card--front card--left">
  <div class="card__header"></div>
  <div class="card__accent" role="img" aria-label="Soft lavender diagonal stripe decoration"></div>
  <p class="brand">Bracken Freight</p>
  <p class="holder">Martin Bracken</p>
  <ul class="contact-list">
    <li>0451 377 208</li>
    <li>1800 419 386</li>
  </ul>
  <p class="website">www.brackenfreight.com.au</p>
</section>

<section class="card card--front card--right">
  <div class="card__header"></div>
  <div class="card__accent" role="img" aria-label="Soft lavender diagonal stripe decoration"></div>
  <p class="brand">Bracken Freight</p>
  <p class="holder">Donna Petherick</p>
  <ul class="contact-list">
    <li>0438 562 714</li>
    <li>1800 419 386</li>
  </ul>
  <p class="website">www.brackenfreight.com.au</p>
</section>

<section class="card card--back card--left">
  <div class="card__header"></div>
  <div class="card__accent" role="img" aria-label="Soft lavender diagonal stripe decoration"></div>
  <p class="brand">Bracken Freight</p>
  <ul class="contact-list">
    <li>1800 419 386</li>
    <li>martin@brackenfreight.com.au</li>
    <li>ABN No - 83 214 976 302</li>
  </ul>
</section>

<section class="card card--back card--right">
  <div class="card__header"></div>
  <div class="card__accent" role="img" aria-label="Soft lavender diagonal stripe decoration"></div>
  <p class="brand">Bracken Freight</p>
  <ul class="contact-list">
    <li>1800 419 386</li>
    <li>donna@brackenfreight.com.au</li>
    <li>ABN No - 83 214 976 302</li>
  </ul>
</section>

</body>
</html>
```